TerraLume Business Card Design Project

We need a business card design for a new company called "TerraLume Systems". TerraLume provides 3D visualization software for subsurface oil and gas data so you can make confident downhole decisions.

Our goal is to provide easy to understand big pictures of your data so your can make confident planning decisions.

Our tagline is
CLEAR SUBSURFACE INSIGHT. SHARED 3D VIEWS. SMARTER WELL PLANNING

Check out http://www.terralume-example.com for more ideas.

The design should promote a technology company that delivers web-based solutions focused on photo-realistic 3D graphics.

The colors from our existing logo (attached) are one option but not a requirement. The design SHOULD NOT use the existing logo.

The design should be two sided and full color. If you require any special print considerations (example: paper type, matte finish, metallic ink, etc) please provide detailed comments. Please also specify any desired details such as rounding of corners, etc.

IF YOU USE BLACK our printer states "We recommend using CMYK black (0, 0, 0, 100) or for a rich black (60, 40, 40, 100). Ensure your artwork is in CMYK mode before adjusting the black."

For design purposes you can use the following contact information

name: Harlan Pike
title: founder
phone: 555.987.6543
email: harlan@terralume-example.com

company information
TerraLume is our "branded" name
"TerraLume Systems" is our official name
www.terralume-example.com

address:
Suite 720
482 Birchmont Avenue SW
Calgary, AB, Canada
T3K 4R8

Target Market(s)

Companies spend a lot of time collecting, organizing and analyzing data but it's really hard to to get a big picture view of current and planned projects, especially in context to existing wellbores, geology and downhole equipment

TerraLume enables you to explore the big picture in an immersive, 3D environment. Our goal is to help transform you rich data into an easily understood picture, to make confident planning decisions and anticipate trouble events before the expensive execution phase.

Industry/Entity Type

Oil And Gas

Requirements
Must have
• The business card design should be sized to a standard 3.5 x 2 inches and print ready. See the attachment for a sample sized card
It MUST meet these requirements:
Exported as PDF file with two pages:
page 1: front design
page 2: back design
All Images must be 300ppi or higher (at 100%)
CMYK colour mode
0.125 inches of bleed on all sides (0.25 inches additional width and height)
0.125 inch safety margin (inside trim line)

```html
<!DOCTYPE html>
<html lang="en">
<head>
<meta charset="utf-8">
<title>TerraLume Systems – Business Card</title>
<link href="https://fonts.googleapis.com/css2?family=Questrial&family=Montserrat:wght@700&display=swap" rel="stylesheet">
<style>
  :root {
    --backdrop: #e9e7e3;
    --lime: #8ef014;
    --lime-light: #a6f53c;
    --lime-deep: #74d40a;
    --ink: #111213;
    --charcoal: #1e2021;
    --slate: #7b8385;
    --slate-dark: #5f6668;
    --steel: #b8bec0;
    --text-dark: #1b1d1e;
  }
  * { box-sizing: border-box; margin: 0; padding: 0; }
  html, body {
    width: 1200px; height: 741px; overflow: hidden;
    background: var(--backdrop);
    font-family: "Questrial", "Century Gothic", sans-serif;
  }
  .sheet {
    width: 1200px; height: 741px;
    display: flex; align-items: center; justify-content: center; gap: 50px;
  }
  .card {
    position: relative;
    width: 540px; height: 309px;
    overflow: hidden;
    box-shadow: 0 10px 28px rgba(0,0,0,.22);
  }

  /* Front */
  .card--front { background: var(--ink); }
  .front__field {
    position: absolute; left: 0; top: 0; width: 100%; height: 168px;
    background: linear-gradient(180deg, var(--lime-light) 0%, var(--lime) 55%, var(--lime-deep) 100%);
  }
  .front__rule {
    position: absolute; left: 0; top: 168px; width: 100%; height: 18px;
    background: var(--charcoal);
    border-top: 1px solid var(--steel);
    display: flex; align-items: center; justify-content: center;
  }
  .tagline {
    color: var(--steel);
    font-size: 8.5px; letter-spacing: 1.6px; text-transform: uppercase;
    white-space: nowrap;
  }
  .front__base {
    position: absolute; left: 0; top: 186px; width: 100%; height: 123px;
    display: flex; align-items: center; justify-content: center; gap: 14px;
  }
  .brand-mark {
    width: 30px; height: 30px; background: var(--slate-dark);
  }
  .brand-name {
    color: var(--lime); font-size: 46px; line-height: 1;
  }

  /* Back */
  .card--back { background: var(--slate); }
  .name-band {
    position: absolute; left: 250px; top: 74px; width: 290px; height: 70px;
    background: var(--lime);
    padding: 12px 0 0 18px;
  }
  .person-name {
    font-family: "Montserrat", "Arial", sans-serif; font-weight: 700;
    font-size: 24px; color: var(--text-dark); line-height: 1.05;
  }
  .person-title {
    font-family: "Montserrat", "Arial", sans-serif; font-weight: 700;
    font-size: 10px; color: var(--text-dark); margin: 6px 0 0 40px;
  }
  .contact {
    position: absolute; left: 26px; top: 42px;
    list-style: none; color: var(--text-dark);
    font-size: 11.5px; line-height: 1.55;
  }
  .back__brand {
    position: absolute; left: 26px; bottom: 22px;
    display: flex; align-items: center; gap: 8px;
  }
  .back__brand .brand-mark { width: 18px; height: 18px; background: var(--steel); }
  .back__brand .brand-name { font-size: 20px; }
</style>
</head>
<body>
<main class="sheet">
  <section class="card card--front" aria-label="Card front">
    <div class="front__field"></div>
    <div class="front__rule">
      <p class="tagline">Clear subsurface insight. Shared 3D views. Smarter well planning</p>
    </div>
    <div class="front__base">
      <span class="brand-mark"></span>
      <span class="brand-name">TerraLume</span>
    </div>
  </section>

  <section class="card card--back" aria-label="Card back">
    <ul class="contact">
      <li>harlan@terralume-example.com</li>
      <li>www.terralume-example.com</li>
      <li>Suite 720 482 Birchmont Avenue SW</li>
      <li>Calgary, AB, Canada T3K 4R8</li>
      <li>555.987.6543</li>
    </ul>
    <div class="name-band">
      <p class="person-name">Harlan Pike</p>
      <p class="person-title">Founder</p>
    </div>
    <div class="back__brand">
      <span class="brand-mark"></span>
      <span class="brand-name">TerraLume</span>
    </div>
  </section>
</main>
</body>
</html>
```